A website for a Maltese Law Firm

Our law firm needs a website to further its business. The site should have a simple yet effective design. We would need the following sections: About us, Practice Areas, About Malta, Contact. These should be further split as follows:

About us: Our firm, Our values, What others say, Offices

Practice Areas: Crimimal, Citizenship & Residence, Harbour Passage Scheme, Criminal Defence, Civil Litigation, Arbitration and ADR, Commercial and Corporate, Media Law.

About Malta: just one section.

Contact: Just one section

We would also need a news feed at the front of the site to include latest news regarding our cases.

At the bottom we need a section for our Terms and a Privacy Statement.

Our logo is being attached.

Target Market(s)

All clients looking for legal assistance in Malta

Industry/Entity Type

Legal

Coding

Coded - Design and coding required

Number of Pages Required

1 page

Requirements
Must have
• It must be simple yet striking.

```html
<!DOCTYPE html>
<html lang="en">
<head>
<meta charset="utf-8">
<title>Caruana &amp; Bonello Advocates</title>
<link href="https://fonts.googleapis.com/css2?family=Marcellus+SC&family=Lato:ital,wght@0,400;0,700;1,400&display=swap" rel="stylesheet">
<style>
:root{
  --ink:#2b2d33;
  --ink-soft:#3a3c42;
  --paper:#ffffff;
  --mist:#ececec;
  --band:#a9aaae;
  --line:#cfcfcf;
  --tab:#c4c4c4;
  --foot-bar:#d4d4d6;
}
*{margin:0;padding:0;box-sizing:border-box}
html,body{width:1200px;height:2723px;overflow:hidden}
body{font-family:"Lato",sans-serif;color:var(--ink);background:var(--paper);position:relative}
a{color:inherit;text-decoration:none}

/* header */
.site-header{position:absolute;top:0;left:0;width:1200px;height:107px;background:var(--paper)}
.brand{position:absolute;left:72px;top:34px;display:flex;align-items:center;gap:12px;font-family:"Lato",sans-serif;font-weight:400;font-size:30px;color:var(--ink);white-space:nowrap}
.brand-mark{width:26px;height:26px;background:var(--ink)}
.header-contact{position:absolute;left:899px;top:22px;font-size:16px;font-weight:700}
.header-contact div{display:flex;align-items:center;gap:10px;height:32px}
.icon-box{width:24px;height:24px;background:var(--ink);border-radius:4px;display:flex;align-items:center;justify-content:center}

/* nav */
.main-nav{position:absolute;top:107px;left:0;width:1200px;height:45px;background:var(--ink);display:flex;padding-left:69px}
.main-nav a{font-family:"Marcellus SC",serif;color:#fff;font-size:15px;height:45px;display:flex;align-items:center;padding:0 24px;border-right:1px solid #6b6d72;letter-spacing:.5px}
.main-nav a.active{background:var(--tab);color:var(--ink)}

/* hero */
.hero{position:absolute;top:152px;left:0;width:1200px;height:425px;background:linear-gradient(100deg,#d8d4cc 0%,#b99a80 30%,#c9b6a2 48%,#6c86a8 62%,#3b3633 82%,#251f1d 100%)}
.hero-title{position:absolute;left:127px;top:310px;font-family:"Marcellus SC",serif;font-size:31px;color:#fff;line-height:1.3;text-shadow:1px 2px 3px rgba(0,0,0,.7)}
.hero-btn{position:absolute;left:783px;top:331px;width:290px;height:51px;background:rgba(43,45,51,.85);border:2px solid #bbb;color:#fff;font-family:"Marcellus SC",serif;font-size:20px;display:flex;align-items:center;justify-content:center}
.hero-arrow{position:absolute;top:170px}

/* welcome */
.welcome{position:absolute;top:577px;left:0;width:1200px;height:454px;background:var(--mist)}
.welcome h1{position:absolute;left:69px;top:58px;font-family:"Marcellus SC",serif;font-weight:400;font-size:30px}
.welcome .lead{position:absolute;left:69px;top:111px;width:660px;font-size:16px;line-height:24px}
.welcome .body{position:absolute;left:69px;top:172px;width:684px;font-size:14px;line-height:22px;color:#333}
.pill{position:absolute;display:flex;align-items:center}
.pill span{background:#b5b5b5;border:1px solid #888;height:28px;display:flex;align-items:center;padding:0 30px 0 10px;font-size:12px;font-weight:700;text-transform:uppercase;color:var(--ink)}
.pill i{width:34px;height:34px;border-radius:50%;background:var(--ink);margin-left:-18px;display:flex;align-items:center;justify-content:center}
.eval{position:absolute;left:797px;top:62px;width:331px;height:325px;border:2px solid var(--ink)}
.eval h2{font-family:"Marcellus SC",serif;font-weight:400;font-size:26px;margin:22px 0 0 17px}
.field{position:absolute;left:18px;width:292px;height:40px;background:#fff;border:1px solid #ccc;font-size:12px;padding:10px}

/* practice areas */
.practice{position:absolute;top:1031px;left:0;width:1200px;height:425px;background:var(--paper)}
.section-title{position:absolute;left:0;width:1200px;text-align:center;font-family:"Marcellus SC",serif;font-size:30px;font-weight:400}
.area{position:absolute;top:122px;width:260px;text-align:center}
.area .tile{width:102px;height:102px;border:2px solid var(--ink);margin:0 auto;display:flex;align-items:center;justify-content:center;background:#fff}
.area .tile.on{background:var(--ink)}
.area h3{font-family:"Marcellus SC",serif;font-weight:400;font-size:21px;margin-top:16px;letter-spacing:.5px}
.area p{font-size:13px;line-height:1.4;margin:10px auto 0;width:190px}
.area .more{font-size:16px;margin-top:12px}
.side-arrow{position:absolute}

/* case studies */
.cases{position:absolute;top:1456px;left:0;width:1200px;height:527px;background:var(--mist)}
.case{position:absolute;top:120px;width:312px}
.case .shot{height:164px;border:6px solid #fff;outline:1px solid var(--line)}
.case .date{position:absolute;left:6px;top:6px;width:42px;background:#fff;text-align:center}
.case .date b{display:block;background:var(--ink);color:#fff;font-size:16px;padding:2px 0}
.case .date span{font-size:13px}
.case h4{font-size:13px;margin-top:20px}
.case p{font-size:12.2px;line-height:20px;margin-top:10px;color:#333}
.case .read{font-size:12.2px;margin-top:10px}

/* testimonials */
.testimonials{position:absolute;top:1983px;left:0;width:1200px;height:300px;background:var(--paper)}
.client-photo{position:absolute;left:136px;top:116px;width:115px;height:116px;background:linear-gradient(180deg,#d7dde4 0%,#b9a99b 55%,#2b3344 100%)}
.quote{position:absolute;left:316px;top:114px;width:760px;text-indent:38px;font-style:italic;font-size:13px;line-height:22px;color:#333}
.quote-mark{position:absolute;font-family:"Marcellus SC",serif;font-size:64px;color:#dcdcdc;line-height:1}
.client-name{position:absolute;left:309px;top:222px;font-family:"Marcellus SC",serif;font-size:18px;letter-spacing:1px}

/* call to action */
.cta{position:absolute;top:2283px;left:0;width:1200px;height:129px;background:var(--band)}
.cta p{position:absolute;left:116px;top:28px;font-family:"Marcellus SC",serif;font-size:30px;color:#fff;line-height:1.2;letter-spacing:.5px}
.cta a{position:absolute;left:844px;top:40px;width:224px;height:47px;background:var(--ink);border:2px solid #ddd;color:#fff;font-weight:700;font-size:23px;display:flex;align-items:center;justify-content:center}

/* footer */
.site-footer{position:absolute;top:2412px;left:0;width:1200px;height:267px;background:var(--ink);color:#fff}
.foot-title{position:absolute;top:44px;font-family:"Marcellus SC",serif;font-size:18px;letter-spacing:.5px;padding-bottom:8px;border-bottom:1px solid #555}
.quick{position:absolute;left:69px;top:86px;list-style:none;font-size:12px;font-weight:700}
.quick li{height:24.5px;display:flex;align-items:center;gap:10px}
.quick li::before{content:"";width:5px;height:5px;background:#fff;border-radius:50%}
.map{position:absolute;left:303px;top:87px;width:259px;height:124px;background:linear-gradient(135deg,#e9e6dc,#d7dcd0 50%,#e4e1d6)}
.addr{position:absolute;left:589px;top:85px;font-size:12px;line-height:1.5}
.addr div{display:flex;gap:12px;margin-bottom:8px}
.addr svg{flex:none;margin-top:2px}
.foot-brand{position:absolute;left:884px;top:98px;width:248px;text-align:center;font-family:"Lato",sans-serif;font-weight:400;font-size:20px;color:#fff;white-space:nowrap}
.socials{position:absolute;left:926px;top:148px;display:flex;gap:10px}
.socials span{width:34px;height:34px;border-radius:50%;background:#fff;border:3px solid #5a5c62}
.divider{position:absolute;left:838px;top:56px;width:1px;height:170px;background:#4a4c52}
.foot-bar{position:absolute;top:2679px;left:0;width:1200px;height:44px;background:var(--foot-bar);font-size:13px;color:var(--ink-soft);display:flex;align-items:center;justify-content:space-between;padding:0 69px}
</style>
</head>
<body>

<header class="site-header">
  <a class="brand" href="#"><span class="brand-mark"></span>Caruana &amp; Bonello Advocates</a>
  <div class="header-contact">
    <div><span class="icon-box"><svg width="14" height="14" viewBox="0 0 14 14"><rect x="3" y="1" width="8" height="12" rx="1.5" fill="none" stroke="#fff" stroke-width="1.5"/><circle cx="7" cy="10.5" r="0.9" fill="#fff"/></svg></span>555-014-2290</div>
    <div><span class="icon-box"><svg width="14" height="14" viewBox="0 0 14 14"><rect x="1" y="3" width="12" height="8" fill="none" stroke="#fff" stroke-width="1.4"/><path d="M1 3l6 5 6-5" fill="none" stroke="#fff" stroke-width="1.4"/></svg></span>info@cbadvocates.example</div>
  </div>
</header>

<nav class="main-nav">
  <a class="active" href="#">Home</a>
  <a href="#">About Malta</a>
  <a href="#">Practice Areas</a>
  <a href="#">Our Firm</a>
  <a href="#">Our Values</a>
  <a href="#">What Others Say</a>
  <a href="#">Contact Us</a>
</nav>

<section class="hero" role="img" aria-label="Photo of smiling clients shaking hands with a lawyer across a desk">
  <svg class="hero-arrow" style="left:28px" width="24" height="90" viewBox="0 0 24 90"><path d="M22 2L3 45l19 43" fill="none" stroke="#fff" stroke-width="2"/></svg>
  <svg class="hero-arrow" style="right:28px" width="24" height="90" viewBox="0 0 24 90"><path d="M2 2l19 43L2 88" fill="none" stroke="#fff" stroke-width="2"/></svg>
  <div class="hero-title">Realize Your Constitutional Right For<br>Qualified Legal Help</div>
  <a class="hero-btn" href="#">Get A Free Consultation</a>
</section>

<section class="welcome">
  <h1>Welcome To Caruana &amp; Bonello Advocates</h1>
  <p class="lead">Lorem ipsum dolor sit amet, consectetuer adipiscing elit, sed diam nonummy nibh euismod tincidunt ut laoreet dolore magna aliquam erat volutpat.</p>
  <p class="body">Lorem ipsum dolor sit amet, consectetur adipiscing elit. Sed vitae magna tellus. Aenean ante nunc, semper nec cursus non, rutrum ac eros. Vestibulum mattis justo ac dui bibendum consequat a ac ipsum. Praesent a arcu venenatis, auctor velit eu, suscipit libero. Quisque convallis, leo ac pharetra sagittis, ipsum arcu auctor urna, sit amet cursus risus augue in eros. Duis lacinia nisi vitae leo commodo, non finibus magna maximus. Sed posuere, neque eget bibendum pulvinar, ligula erat suscipit dolor, ut maximus arcu mi et tortor. Quisque imperdiet turpis et ligula mollis ultricies. Mauris lacinia rhoncus odio, at rutrum diam mollis eu. Quisque ut ipsum faucibus, tristique dui vitae, posuere orci.</p>
  <a class="pill" href="#" style="left:69px;top:358px"><span>Read More</span><i><svg width="10" height="14" viewBox="0 0 10 14"><path d="M2 1l6 6-6 6" fill="none" stroke="#fff" stroke-width="2"/></svg></i></a>

  <form class="eval">
    <h2>Free Case Evaluation</h2>
    <div class="field" style="top:80px">Name</div>
    <div class="field" style="top:129px">Email</div>
    <div class="field" style="top:178px;height:76px">Message</div>
    <a class="pill" href="#" style="left:18px;top:271px"><span style="font-size:14px;padding-right:34px">Submit</span><i style="width:38px;height:38px"><svg width="10" height="14" viewBox="0 0 10 14"><path d="M2 1l6 6-6 6" fill="none" stroke="#fff" stroke-width="2"/></svg></i></a>
  </form>
</section>

<section class="practice">
  <h2 class="section-title" style="top:52px">Our Practice Areas</h2>
  <svg class="side-arrow" style="left:30px;top:215px" width="16" height="56" viewBox="0 0 16 56"><path d="M14 2L2 28l12 26" fill="none" stroke="#555" stroke-width="2"/></svg>
  <svg class="side-arrow" style="right:30px;top:215px" width="16" height="56" viewBox="0 0 16 56"><path d="M2 2l12 26L2 54" fill="none" stroke="#555" stroke-width="2"/></svg>

  <div class="area" style="left:70px">
    <div class="tile"><svg width="56" height="40" viewBox="0 0 56 40"><circle cx="16" cy="24" r="10" fill="none" stroke="#2b2d33" stroke-width="4"/><circle cx="40" cy="24" r="10" fill="none" stroke="#2b2d33" stroke-width="4"/><path d="M24 16q4-10 8 0" fill="none" stroke="#2b2d33" stroke-width="3"/><rect x="10" y="8" width="8" height="6" fill="#2b2d33"/><rect x="38" y="8" width="8" height="6" fill="#2b2d33"/></svg></div>
    <h3>Crimimal</h3>
    <p>Lorem ipsum dolor sit amet, consectetuer Lorem dolor sit amet, consectetuer</p>
    <div class="more">[+]</div>
  </div>
  <div class="area" style="left:329px">
    <div class="tile on"><svg width="34" height="46" viewBox="0 0 34 46"><rect x="1" y="1" width="32" height="44" rx="3" fill="#fff"/><circle cx="17" cy="18" r="8" fill="none" stroke="#2b2d33" stroke-width="2"/><path d="M9 18h16M17 10v16M12 12q5 6 0 12M22 12q-5 6 0 12" fill="none" stroke="#2b2d33" stroke-width="1.3"/><rect x="10" y="34" width="14" height="3" fill="#2b2d33"/></svg></div>
    <h3>Citizenship &amp; Residence</h3>
    <p>Lorem ipsum dolor sit amet, consectetuer Lorem dolor sit amet, consectetuer</p>
    <div class="more">[+]</div>
  </div>
  <div class="area" style="left:600px">
    <div class="tile"><svg width="56" height="50" viewBox="0 0 56 50"><path d="M4 10h48M4 20h48M4 30h48M4 40h48" stroke="#2b2d33" stroke-width="1.5"/><circle cx="28" cy="14" r="7" fill="#2b2d33"/><path d="M14 42q0-20 14-20t14 20z" fill="#2b2d33"/><rect x="18" y="26" width="20" height="12" fill="#fff" stroke="#2b2d33" stroke-width="2"/></svg></div>
    <h3>Criminal Defence</h3>
    <p>Lorem ipsum dolor sit amet, consectetuer Lorem dolor sit amet, consectetuer</p>
    <div class="more">[+]</div>
  </div>
  <div class="area" style="left:872px">
    <div class="tile"><svg width="52" height="50" viewBox="0 0 52 50"><g transform="rotate(-40 24 16)"><rect x="12" y="4" width="24" height="14" fill="#2b2d33"/><rect x="22" y="18" width="4" height="26" fill="#2b2d33"/></g><rect x="4" y="42" width="30" height="5" fill="#2b2d33"/></svg></div>
    <h3>Civil Litigation</h3>
    <p>Lorem ipsum dolor sit amet, consectetuer Lorem dolor sit amet, consectetuer</p>
    <div class="more">[+]</div>
  </div>
</section>

<section class="cases">
  <h2 class="section-title" style="top:50px">Case Studies</h2>
  <article class="case" style="left:69px">
    <div class="shot" role="img" aria-label="Photo of rows of leather-bound law books" style="background:linear-gradient(90deg,#3a2414,#8a5a2a,#c39a52,#6a3a1c,#b3883e,#3a2414)"></div>
    <div class="date"><b>06</b><span>Jun</span></div>
    <h4>Lorem Ipsum Dolor Sit Amet &nbsp;Consectetur</h4>
    <p>Lorem ipsum dolor sit amet, consectetur adipiscing elit. Sed vitae magna tellus. Aenean ante nunc, semper nec cursus non, rutrum ac eros.</p>
    <div class="read">Read More ››</div>
  </article>
  <article class="case" style="left:444px">
    <div class="shot" role="img" aria-label="Photo of a handcuffed defendant standing in a courtroom" style="background:linear-gradient(90deg,#5a2a16,#8a4a28 35%,#2a2a2e 55%,#3a3a40 80%,#6a3a20)"></div>
    <div class="date"><b>06</b><span>Jun</span></div>
    <h4>Lorem Ipsum Dolor Sit Amet &nbsp;Consectetur</h4>
    <p>Lorem ipsum dolor sit amet, consectetur adipiscing elit. Sed vitae magna tellus. Aenean ante nunc, semper nec cursus non, rutrum ac eros.</p>
    <div class="read">Read More ››</div>
  </article>
  <article class="case" style="left:819px">
    <div class="shot" role="img" aria-label="Photo of a hand signing a document on a desk" style="background:linear-gradient(135deg,#2a2a2c,#7a7a7e 40%,#e8e6e2 70%,#cfcac2)"></div>
    <div class="date"><b>07</b><span>Jun</span></div>
    <h4>Lorem Ipsum Dolor Sit Amet &nbsp;Consectetur</h4>
    <p>Lorem ipsum dolor sit amet, consectetur adipiscing elit. Sed vitae magna tellus. Aenean ante nunc, semper nec cursus non, rutrum ac eros.</p>
    <div class="read">Read More ››</div>
  </article>
  <a class="pill" href="#" style="left:537px;top:448px"><span style="padding:0 34px 0 16px">View All</span><i><svg width="10" height="14" viewBox="0 0 10 14"><path d="M2 1l6 6-6 6" fill="none" stroke="#fff" stroke-width="2"/></svg></i></a>
</section>

<section class="testimonials">
  <h2 class="section-title" style="top:52px">Client Testimonials</h2>
  <svg class="side-arrow" style="left:30px;top:140px" width="16" height="56" viewBox="0 0 16 56"><path d="M14 2L2 28l12 26" fill="none" stroke="#555" stroke-width="2"/></svg>
  <svg class="side-arrow" style="right:30px;top:140px" width="16" height="56" viewBox="0 0 16 56"><path d="M2 2l12 26L2 54" fill="none" stroke="#555" stroke-width="2"/></svg>
  <div class="client-photo" role="img" aria-label="Portrait photo of the client in a suit"></div>
  <span class="quote-mark" style="left:308px;top:100px">“</span>
  <p class="quote">Lorem ipsum dolor sit amet, consectetuer adipiscing elit, sed diam nonummy nibh euismod tincidunt ut laoreet dolore magna aliquam erat volutpat. Ut wisi enim ad minim veniam, quis nostrud exerci iriure dolor in Lorem ipsum dolor sit amet, consectetuer adipiscing elit, sed diam nonummy nibh euismod tincidunt ut laoreet dolore magna aliquam erat volutpat. Ut wisi enim ad minim veniam, quis nostrud exerci iriure dolo.</p>
  <span class="quote-mark" style="left:538px;top:176px">”</span>
  <div class="client-name">- Daniel Marsh</div>
</section>

<section class="cta">
  <p>For Any Legal Problem, We Can Help You<br>Anytime take An Appointment Now</p>
  <a href="#">CONTACT US</a>
</section>

<footer class="site-footer">
  <div class="foot-title" style="left:69px;width:140px">Quick Links</div>
  <ul class="quick">
    <li>Home</li><li>About Malta</li><li>Practice Areas</li><li>Our Firm</li><li>Our Values</li><li>What Others Say</li><li>Contact Us</li>
  </ul>
  <div class="foot-title" style="left:301px;width:490px">Contact Details</div>
  <div class="map" role="img" aria-label="Street map showing the office location"></div>
  <div class="addr">
    <div><svg width="12" height="16" viewBox="0 0 12 16"><path d="M6 15S1 9 1 6a5 5 0 0110 0c0 3-5 9-5 9z" fill="#fff"/><circle cx="6" cy="6" r="2" fill="#2b2d33"/></svg><span><b>Caruana &amp; Bonello Advocates</b><br>12/4, Harbour Lane, Valletta<br>88, Orchard Street, Mosta</span></div>
    <div><svg width="14" height="14" viewBox="0 0 14 14"><path d="M3 1l3 3-2 2q2 3 4 4l2-2 3 3-2 2Q5 12 1 3z" fill="#fff"/></svg>555-014-2290</div>
    <div><svg width="14" height="14" viewBox="0 0 14 14"><rect x="3" y="1" width="8" height="4" fill="#fff"/><rect x="1" y="5" width="12" height="6" fill="#fff"/><rect x="3" y="9" width="8" height="4" fill="#fff" stroke="#2b2d33"/></svg>555-014-2291</div>
    <div><svg width="14" height="12" viewBox="0 0 14 12"><rect x="1" y="2" width="12" height="8" fill="#fff"/><path d="M1 2l6 5 6-5" fill="none" stroke="#2b2d33" stroke-width="1.2"/></svg>info@cbadvocates.example</div>
  </div>
  <div class="divider"></div>
  <div class="foot-brand">Caruana &amp; Bonello Advocates</div>
  <div class="socials"><span></span><span></span><span></span><span></span></div>
</footer>
<div class="foot-bar">
  <span>Copyright © 2016 <b>Caruana &amp; Bonello Advocates</b>. All Rights Reserved.</span>
  <span>Terms &amp; Conditions &nbsp;| &nbsp;Privacy Policy &nbsp;| &nbsp;Disclaimer</span>
</div>

</body>
</html>
```